We are a bed retailer and require a Banner for my new website which stands out from the crowd.

The banner i require should be bold, Colours dark and light blues and yellow / orange like my logo attached. Also i have attached some ideas of other banners within the website in regqrds to syle im looking for.

The banner should include the following text.
INSTORE ONLY!!
TOP BRANDED, TOP QUALITY BEDS & MATTRESSES ALL SOLD AS ONE OFF, ONE ONLY, GIVEAWAY BARGAINS!
SAVE UPTO 80% OFF R.R.P. DON'T MISS OUT! PRICES WON'T BE BEATEN.

Banner size
width: 2000 pixels
height: 335 pixels.

To look like a high impact sale banner can use red colours

Font styles to use
Sans Serif

Colors
0655a3
ec1f27
33a6d7
ffc214

Requirements
Must have
• High impact like a sale banner!!

```html
<!DOCTYPE html>
<html lang="en">
<head>
<meta charset="utf-8">
<title>In Store Only – Bed &amp; Mattress Sale Banner</title>
<link rel="stylesheet" href="https://fonts.googleapis.com/css2?family=Roboto:wght@700;900&display=swap">
<style>
  :root {
    --sale-red: #ec1f27;
    --navy: #0b3f78;
    --brand-blue: #0655a3;
    --mid-blue: #1a6ebb;
    --sky-blue: #33a6d7;
    --sun-yellow: #ffc214;
    --white: #ffffff;
    --mattress-light: #f4f4f4;
    --mattress-shade: #c9ccd1;
  }
  * { margin: 0; padding: 0; box-sizing: border-box; }
  html, body { width: 1200px; height: 201px; overflow: hidden; background: var(--white); }
  .banner {
    position: relative;
    width: 1200px;
    height: 201px;
    overflow: hidden;
    font-family: "Roboto", "Arial Black", sans-serif;
    background: var(--white);
  }
  .banner__backdrop { position: absolute; inset: 0; }
  .banner__mascot {
    position: absolute;
    left: 8px; top: 4px;
    width: 150px; height: 190px;
    border-radius: 40px 40px 20px 20px;
    background: linear-gradient(180deg, var(--sky-blue), var(--brand-blue));
  }
  .banner__mattresses {
    position: absolute;
    left: 135px; top: 0;
    width: 265px; height: 201px;
    clip-path: polygon(10% 0, 78% 0, 100% 100%, 0 100%);
    background: linear-gradient(160deg, var(--white) 0%, var(--mattress-light) 55%, var(--mattress-shade) 100%);
  }
  .banner__stack {
    position: absolute;
    right: 0; top: 0;
    width: 92px; height: 201px;
    background: linear-gradient(90deg, var(--mattress-light), var(--white) 40%, var(--mattress-shade));
  }
  .banner__copy {
    position: absolute;
    left: 400px; width: 700px;
    top: 0; height: 201px;
    text-align: center;
    color: var(--white);
    text-transform: uppercase;
    white-space: nowrap;
  }
  .headline {
    position: absolute; left: 0; right: 0; top: 4px;
    font-weight: 900; font-size: 48px; line-height: 1; letter-spacing: 0.5px;
  }
  .subline {
    position: absolute; left: 0; right: 0; top: 50px;
    font-weight: 900; font-size: 20px; line-height: 27px; letter-spacing: 0.4px;
  }
  .offer {
    position: absolute; left: 0; right: 0; top: 124px;
    font-weight: 900; font-size: 32px; line-height: 1; letter-spacing: 0.6px;
  }
  .promise {
    position: absolute; left: 0; right: 0; top: 157px;
    font-weight: 900; font-size: 36px; line-height: 1; letter-spacing: 1.2px;
  }
  .accent { color: var(--sun-yellow); }
</style>
</head>
<body>
  <div class="banner">
    <svg class="banner__backdrop" width="1200" height="201" viewBox="0 0 1200 201" aria-hidden="true">
      <rect x="0" y="0" width="1200" height="201" fill="var(--white)"/>
      <rect x="0" y="0" width="380" height="201" fill="var(--sale-red)"/>
      <polygon points="336,0 1136,0 1112,201 394,201" fill="var(--sky-blue)"/>
      <polygon points="346,0 1132,0 1108,201 404,201" fill="var(--mid-blue)"/>
      <polygon points="346,0 1132,0 1119,108 384,108" fill="var(--navy)"/>
    </svg>
    <div class="banner__mattresses" role="img" aria-label="Stack of white quilted mattresses"></div>
    <div class="banner__mascot" role="img" aria-label="Cartoon mattress mascot character waving"></div>
    <div class="banner__stack" role="img" aria-label="Tall stack of white mattresses"></div>

    <div class="banner__copy">
      <h1 class="headline">In Store <span class="accent">Only!!</span></h1>
      <p class="subline">Top branded, top quality beds &amp; mattresses<br>All sold as one off, one only, giveaway bargains!</p>
      <p class="offer"><span class="accent">Save up to 80%</span> off R.R.P. <span class="accent">Don't miss out!</span></p>
      <p class="promise">Prices <span class="accent">won't</span> be beaten</p>
    </div>
  </div>
</body>
</html>
```